Create Vertical Dog Food Labels (3 inches x 5 inches) for Pawlyn Kitchen

We need a packing Vertical label (3 inches x 5 inches) design for our line of Dog Food - Pawlyn Kitchen at pawlynkitchen.com (please review website). This design is for Custom Roll Labels. We have a logo already. Use our logo colors on label. What we need incorporated is a list of our ingredients:

50% Choice Beef
20% Pasture-raised Chicken
15% Brown Rice
15% Fresh Vegetables - Carrots, Kale, Zucchini
Herbal Health Boosters

We also need these lines at the bottom of the label:

Keeps in fridge for 4 days after thawing
Stores in freezer up to 6 months
Questions? email us at orders@brindlecopsepantry.com

We have attached a sample of a competitor. The Meadow Bowl.

Target Market(s)

Dog owners

Industry/Entity Type

Dog Food

Font styles to use
Sans Serif

Requirements
Must have
• Read project description above
Nice to have
• Our logo color incorporated
Should not have
• I want it simple.

```html
<!DOCTYPE html>
<html lang="en">
<head>
<meta charset="utf-8">
<title>Pawlyn Kitchen – Vertical Dog Food Label 3 × 5 in</title>
<link rel="stylesheet" href="https://fonts.googleapis.com/css2?family=Montserrat:wght@500;600;700&family=Open+Sans:wght@400&display=swap">
<style>
  :root {
    --beef: #ee7a4c;
    --chicken: #f6ac2a;
    --rice: #f1c264;
    --veg: #8bbf5a;
    --herbal: #6aa85b;
    --brand-green: #078c47;
    --trim: #f29bc8;
    --ink: #111111;
    --paper: #ffffff;
  }
  * { box-sizing: border-box; margin: 0; padding: 0; }
  html, body { width: 1200px; height: 1000px; overflow: hidden; background: var(--paper); }
  .artboard { position: relative; width: 1200px; height: 1000px; font-family: "Montserrat", sans-serif; }

  /* dimension callouts */
  .dimensions { position: absolute; left: 0; top: 0; }
  .dim-label { position: absolute; font-family: "Open Sans", sans-serif; font-size: 13px; color: var(--ink); white-space: nowrap; }
  .dim-label--width { left: 610px; top: 291px; transform: translateX(-50%); }
  .dim-label--height { left: 480px; top: 500px; transform: translate(-50%, -50%) rotate(-90deg); }

  /* label */
  .label-trim { position: absolute; left: 503px; top: 320px; width: 215px; height: 360px; border: 0.6px solid var(--trim); }

  .brand { position: absolute; left: 503px; top: 346px; width: 215px; text-align: center; }
  .brand-dot { display: block; margin: 0 auto 14px; width: 72px; height: 72px; border-radius: 50%; border: 6px solid var(--veg); }
  .brand-name { font-size: 20px; font-weight: 700; color: var(--brand-green); letter-spacing: -0.2px; line-height: 1; }

  .ingredient { position: absolute; left: 493px; width: 234px; height: 18px; }
  .ingredient-box { position: absolute; inset: 0; border: 0.8px dashed currentColor; }
  .ingredient-pct { position: absolute; left: 0; top: 0; height: 18px; display: flex; align-items: center; justify-content: center; color: var(--paper); font-weight: 700; font-size: 9.5px; }
  .ingredient-name { position: absolute; top: 0; height: 18px; display: flex; align-items: center; font-size: 7px; font-weight: 500; white-space: nowrap; transform: translateX(-50%); }

  .ingredient--beef { top: 486px; color: var(--beef); }
  .ingredient--beef .ingredient-pct { width: 118px; background: var(--beef); }
  .ingredient--beef .ingredient-name { left: 172px; }

  .ingredient--chicken { top: 512px; color: var(--chicken); }
  .ingredient--chicken .ingredient-pct { width: 53px; background: var(--chicken); }
  .ingredient--chicken .ingredient-name { left: 139px; }

  .ingredient--rice { top: 538px; color: var(--rice); }
  .ingredient--rice .ingredient-pct { width: 42px; background: var(--rice); }
  .ingredient--rice .ingredient-name { left: 133px; }

  .ingredient--veg { top: 565px; color: var(--veg); }
  .ingredient--veg .ingredient-pct { width: 42px; background: var(--veg); }
  .ingredient--veg .ingredient-name { left: 133px; }

  .herbal-band { position: absolute; left: 493px; top: 591px; width: 234px; height: 18px; background: var(--herbal); color: var(--paper); font-size: 7px; font-weight: 500; display: flex; align-items: center; justify-content: center; }

  .storage-band { position: absolute; left: 493px; top: 632px; width: 234px; height: 24px; background: var(--brand-green); color: var(--paper); font-size: 6.6px; font-weight: 500; line-height: 8.2px; text-align: center; display: flex; flex-direction: column; justify-content: center; }

  .contact { position: absolute; left: 493px; top: 664px; width: 234px; text-align: center; font-size: 6.6px; font-weight: 500; color: var(--brand-green); white-space: nowrap; }
  .contact strong { font-weight: 700; }
</style>
</head>
<body>
<main class="artboard">
  <svg class="dimensions" width="1200" height="1000" viewBox="0 0 1200 1000" aria-hidden="true">
    <g stroke="#111" stroke-width="0.8" fill="none">
      <line x1="503" y1="311" x2="718" y2="311"/>
      <line x1="503" y1="311" x2="503" y2="320"/>
      <line x1="718" y1="311" x2="718" y2="320"/>
      <line x1="493" y1="321" x2="493" y2="680"/>
      <line x1="493" y1="321" x2="503" y2="321"/>
      <line x1="493" y1="680" x2="503" y2="680"/>
    </g>
    <g fill="#111">
      <polygon points="503,311 512,306.5 512,315.5"/>
      <polygon points="718,311 709,306.5 709,315.5"/>
      <polygon points="493,321 488.5,330 497.5,330"/>
      <polygon points="493,680 488.5,671 497.5,671"/>
    </g>
  </svg>
  <span class="dim-label dim-label--width">3 inch</span>
  <span class="dim-label dim-label--height">5 inch</span>

  <div class="label-trim"></div>

  <header class="brand">
    <span class="brand-dot"></span>
    <h1 class="brand-name">Pawlyn Kitchen</h1>
  </header>

  <div class="ingredient ingredient--beef">
    <span class="ingredient-box"></span>
    <span class="ingredient-pct">50%</span>
    <span class="ingredient-name">Choice Beef</span>
  </div>
  <div class="ingredient ingredient--chicken">
    <span class="ingredient-box"></span>
    <span class="ingredient-pct">20%</span>
    <span class="ingredient-name">Pasture-raised Chicken</span>
  </div>
  <div class="ingredient ingredient--rice">
    <span class="ingredient-box"></span>
    <span class="ingredient-pct">15%</span>
    <span class="ingredient-name">15% Brown Rice</span>
  </div>
  <div class="ingredient ingredient--veg">
    <span class="ingredient-box"></span>
    <span class="ingredient-pct">15%</span>
    <span class="ingredient-name">15% Fresh Vegetables - Carrots, Kale, Zucchini</span>
  </div>

  <div class="herbal-band">Herbal Health Boosters</div>

  <div class="storage-band">
    <span>Keeps in fridge for 4 days after thawing</span>
    <span>Stores in freezer up to 6 months</span>
  </div>

  <p class="contact"><strong>Questions?</strong> email us at orders@brindlecopsepantry.com</p>
</main>
</body>
</html>
```